Wine Bottle Label Logo Design

My fiancé and I are getting married in September and we made homemade wine which will be given to the guests as a wedding favor. We need label/logo for our wine bottles. We were looking for something rustic yet modern and simple. We had an idea for beige and cranberry colored wine stained, weathered, imperfect heart. Things that will need to be incorporated into the label design are as follows:
Our last name and also the name of the wine: Bastoni
The year: 2012
Where is says Alcohol Content on a wine bottle normally write: Alcohol: Deceiving% by vol.
Type of wine: Red Wine
Incorporate our wedding date: Foot Stomped and Bottled for Jess and Ned's Wedding Day 9/28/13

```html
<!DOCTYPE html>
<html lang="en">
<head>
<meta charset="utf-8">
<title>Bastoni Red Wine Label</title>
<link rel="stylesheet" href="https://fonts.googleapis.com/css2?family=Jost:wght@400;500&display=swap">
<style>
  :root {
    --page: #ffffff;
    --label-cream: #fdf9dc;
    --label-edge: #9a9a94;
    --cranberry: #7a2626;
    --rose: #b0678f;
    --blush: #d9a3bf;
  }
  * { margin: 0; padding: 0; box-sizing: border-box; }
  html, body {
    width: 1200px;
    height: 1000px;
    overflow: hidden;
    background: var(--page);
  }
  body {
    position: relative;
    font-family: "Jost", "Futura", sans-serif;
    color: var(--cranberry);
  }
  .wine-label {
    position: absolute;
    left: 150px;
    top: 191px;
    width: 357px;
    height: 641px;
    background: var(--label-cream);
    border: 1px solid var(--label-edge);
    border-radius: 14px;
    text-align: center;
  }
  .vintage {
    position: absolute;
    top: 18px;
    width: 100%;
    font-size: 23px;
    line-height: 30px;
    font-weight: 400;
  }
  .brand {
    position: absolute;
    top: 90px;
    left: 0;
    width: 100%;
    height: 400px;
    display: flex;
    flex-direction: column;
    align-items: center;
    justify-content: center;
    gap: 28px;
  }
  .brand-dot {
    width: 120px;
    height: 120px;
    border-radius: 50%;
    background: var(--blush);
  }
  .brand-name {
    font-size: 66px;
    font-weight: 500;
    line-height: 1;
    color: var(--cranberry);
  }
  .tasting-note {
    position: absolute;
    top: 490px;
    width: 100%;
    font-size: 14.5px;
    line-height: 18px;
  }
  .dedication {
    position: absolute;
    top: 548px;
    width: 100%;
    font-size: 15px;
    line-height: 20px;
    color: var(--rose);
  }
  .alcohol {
    position: absolute;
    top: 607px;
    width: 100%;
    font-size: 11.5px;
  }
  .corner-mark {
    position: absolute;
    left: 1060px;
    top: 45px;
    width: 100px;
    height: 150px;
    display: flex;
    flex-direction: column;
    align-items: center;
    justify-content: center;
    gap: 12px;
  }
  .corner-mark .brand-dot { width: 48px; height: 48px; }
  .corner-mark .brand-name { font-size: 27px; }
</style>
</head>
<body>
  <section class="wine-label">
    <h1 class="vintage">2012<br>RED WINE</h1>
    <div class="brand">
      <span class="brand-dot"></span>
      <span class="brand-name">Bastoni</span>
    </div>
    <p class="tasting-note">Aged outdoors during the cold winter months<br>to allow for a slower fermentation process.<br>Its like a warm sweet hug in a bottle.</p>
    <p class="dedication">Foot Stomped and Bottled for<br>Jess and Ned's Wedding Day 9/28/13</p>
    <p class="alcohol">Alcohol: Deceiving % by vol.</p>
  </section>

  <div class="corner-mark">
    <span class="brand-dot"></span>
    <span class="brand-name">Bastoni</span>
  </div>
</body>
</html>
```